Website for IT consulting Company

I need a website upgrade, the existing site content is ok, I would also like to add a testimonial page, the site should be something that is easy for us to update content. You use the content from www.velmarketa.com as an example. I will also post update logo and artwork. I also need a contact form with some type of validation or captcha.

Please omit Address maps

Target Market(s)

small business, service oriented companies. We provide IT Consulting, support and mangement

Industry/Entity Type

Information Technology

Coding

Coded - Design and coding required

Number of Pages Required

1 page

Font styles to use
Serif
Sans Serif

Requirements
Must have
• Contain logo attached, and content from existing web site www.velmarketa.com.
• Also need to update content easily, and be movable to different platforms.
• There is a catch phrase
• "Let us worry about your technology…” “ so you don’t have to!”
• Should be included.
Nice to have
• Testimonial page, Project page where we can post new and past projects and pictures
Should not have
• none

```html
<!DOCTYPE html>
<html lang="en">
<head>
<meta charset="utf-8">
<title>Velmarketa — IT Consulting</title>
<link href="https://fonts.googleapis.com/css2?family=Lato:wght@400;700;900&family=Russo+One&display=swap" rel="stylesheet">
<style>
:root{
  --orange:#f07f1e;
  --orange-dark:#d96a0c;
  --ink:#1d1d1d;
  --text:#3a3a3a;
  --muted:#8a8a8a;
  --line:#dcdcdc;
  --panel:#efefef;
  --white:#ffffff;
  --footer:#141618;
  --hero-a:#3b3e42;
  --hero-b:#1c1e21;
}
*{box-sizing:border-box;margin:0;padding:0}
html,body{width:1200px;height:3622px;overflow:hidden}
body{font-family:"Lato",sans-serif;color:var(--text);background:var(--white);position:relative}
.abs{position:absolute}
.brand{display:flex;align-items:center;gap:10px;font-family:"Lato",sans-serif;font-weight:900;color:var(--orange);letter-spacing:1px}
.brand-mark{width:26px;height:26px;background:var(--orange)}
.section-title{font-family:"Russo One",sans-serif;font-size:34px;color:var(--ink);text-align:center;display:flex;align-items:center;justify-content:center;gap:26px;letter-spacing:1px}
.section-title::before,.section-title::after{content:"";width:110px;height:7px;border-top:1px solid var(--orange);border-bottom:1px solid var(--orange)}

/* header */
.site-header{top:0;left:0;width:1200px;height:92px;background:var(--white);display:flex;align-items:center;justify-content:space-between;padding:0 100px}
.site-header .brand{font-size:34px}
.main-nav{display:flex;align-items:center;gap:22px;font-weight:900;font-size:15px;color:#333;text-transform:uppercase}
.main-nav .home{width:22px;height:22px}

/* hero */
.hero{top:92px;left:0;width:1200px;height:560px;background:radial-gradient(ellipse at 50% 40%,#9aa6b2 0,#5d646b 22%,var(--hero-a) 45%,var(--hero-b) 100%)}
.hero-arrow{top:320px;width:22px;height:42px;background:rgba(255,255,255,.25);display:flex;align-items:center;justify-content:center}
.hero-mission{top:495px;left:0;width:1200px;height:157px;background:rgba(240,127,30,.92);color:var(--white);font-weight:700;font-size:27px;line-height:38px;text-align:center;padding-top:36px}

/* welcome */
.welcome-title{top:700px;left:0;width:1200px}
.welcome-title .brand{font-size:36px;font-family:"Russo One",sans-serif;font-weight:400}
.welcome-sub{top:776px;left:0;width:1200px;text-align:center;font-size:22px;font-weight:700;color:var(--ink)}
.welcome-sub span{color:var(--orange)}
.welcome-copy{top:815px;left:105px;width:990px;font-size:15.5px;line-height:23.5px;text-align:center}
.welcome-copy p+p{margin-top:10px}
.welcome-copy .lead{font-weight:700;color:var(--ink)}
.btn-outline{top:1048px;left:514px;width:172px;height:42px;border:2px solid #555;border-radius:4px;font-weight:700;font-size:17px;color:var(--ink);display:flex;align-items:center;justify-content:center;gap:10px}
.divider{left:0;width:1200px;height:1px;background:#ececec}

/* services */
.services-title{top:1172px;left:0;width:1200px}
.services-intro{top:1238px;left:110px;width:980px;text-align:center;font-size:15.5px;line-height:23px}
.service{font-size:14px;line-height:20px;color:#333}
.service h3{font-size:19px;font-weight:700;color:var(--ink);margin-bottom:2px;text-transform:uppercase}
.service.support h3{color:var(--orange)}
.service.support{color:#b3b3b3}

/* gallery */
.gallery{top:1678px;left:0;width:1200px;height:370px;background:var(--panel)}
.gallery-title{top:1718px;left:0;width:1200px}
.gallery-item{top:1792px;width:216px}
.gallery-photo{width:216px;height:142px}
.gallery-item p{font-size:13.5px;line-height:19px;text-align:center;margin-top:18px;color:#444}
.gallery-item.active .gallery-photo{border:3px solid #888;box-shadow:0 2px 6px rgba(0,0,0,.3);position:relative}
.gallery-item.active .gallery-photo span{position:absolute;top:56px;width:100%;text-align:center;color:var(--white);font-weight:700;font-size:17px}
.side-arrow{width:14px;height:24px}

/* testimonials */
.testi-title{top:2080px;left:0;width:1200px}
.testi-card{top:2150px;width:480px;height:205px;border:1px solid #e2e2e2;background:var(--white);padding:28px 30px 0 30px;font-size:13.5px;line-height:21px;color:#444;box-shadow:0 1px 3px rgba(0,0,0,.06)}
.testi-card .q{position:absolute;left:16px;top:14px;font-family:Georgia,serif;font-size:40px;color:#ddd;line-height:1}
.avatar{top:2322px;width:108px;height:108px;border-radius:50%;border:5px solid var(--white);box-shadow:0 1px 4px rgba(0,0,0,.25)}
.testi-name{top:2390px;font-size:13px;font-weight:700;color:var(--ink)}

/* news */
.news-title{top:2522px;left:0;width:1200px}
.news-card{top:2596px;width:318px;height:326px;background:var(--white);border:1px solid #e6e6e6;box-shadow:0 1px 3px rgba(0,0,0,.06)}
.news-photo{width:100%;height:177px}
.news-body{position:relative;padding:18px 18px 0 78px;font-size:13.5px;line-height:20px}
.news-date{position:absolute;left:16px;top:18px;width:44px;text-align:center;font-size:11px;font-weight:700}
.news-date b{display:block;background:var(--orange);color:var(--white);font-size:14px;padding:3px 0}
.news-date i{display:block;font-style:normal;color:#555;padding-top:3px}
.news-body h4{font-size:14.5px;font-weight:400;color:var(--orange)}
.news-meta{font-size:13px;color:#777;margin-bottom:14px}
.news-meta span{color:var(--orange)}

/* call back */
.callback{top:2982px;left:0;width:1200px;height:283px;background:var(--panel)}
.callback h2{top:3026px;left:100px;font-family:"Russo One",sans-serif;font-weight:400;font-size:36px;line-height:40px;color:var(--ink);letter-spacing:1px}
.callback-copy{top:3124px;left:100px;width:270px;font-size:13.5px;line-height:20px;color:#333}
.form-label{top:3026px;left:458px;font-size:14px;font-weight:700;color:var(--ink)}
.field{width:318px;height:44px;background:var(--white);border:1px solid #e0e0e0;font-size:12px;color:#aaa;padding:14px 12px}
.submit{top:3164px;left:458px;width:164px;height:44px;border:2px solid #555;border-radius:3px;font-size:19px;font-weight:700;color:var(--ink);display:flex;align-items:center;justify-content:center;background:var(--white)}

/* footer */
.site-footer{top:3265px;left:0;width:1200px;height:357px;background:linear-gradient(180deg,#1e2124 0,var(--footer) 55%,#0b0c0d 100%)}
.footer-contact{top:3350px;font-size:12.5px;color:#d9d9d9;text-align:center;width:320px}
.footer-contact svg{display:block;margin:0 auto 14px}
.footer-brand{top:3422px;left:0;width:1200px;display:flex;justify-content:center}
.footer-brand .brand{font-size:40px}
.social{top:3510px;left:0;width:1200px;display:flex;justify-content:center;gap:14px}
.social span{width:34px;height:34px;border-radius:50%;background:var(--white);opacity:.9}
.social span:nth-child(1),.social span:nth-child(3){background:#2e7fc4;opacity:1}
.social span:nth-child(2){background:#2372b0;opacity:1}
.social span:nth-child(4){background:#d9482f;opacity:1}
.copyright{top:3583px;left:0;width:1200px;text-align:center;font-size:13px;color:#cfcfcf}
</style>
</head>
<body>

<header class="site-header abs">
  <div class="brand"><span class="brand-mark"></span>VELMARKETA</div>
  <nav class="main-nav">
    <svg class="home" viewBox="0 0 24 24"><path d="M3 12 12 4l9 8M6 10v10h12V10" fill="none" stroke="#f07f1e" stroke-width="2.4"/></svg>
    <span>About</span><span>Services</span><span>Projects</span><span>Career</span><span>Testimonials</span><span>Contact</span>
  </nav>
</header>

<section class="hero abs" role="img" aria-label="City skyline seen through a light bulb, surrounded by chalk sketches of business and technology ideas"></section>
<div class="hero-arrow abs" style="left:0"><svg width="10" height="16" viewBox="0 0 10 16"><path d="M8 2 2 8l6 6" stroke="#fff" stroke-width="2" fill="none"/></svg></div>
<div class="hero-arrow abs" style="right:0"><svg width="10" height="16" viewBox="0 0 10 16"><path d="M2 2l6 6-6 6" stroke="#fff" stroke-width="2" fill="none"/></svg></div>
<div class="hero-mission abs">Our Mission Is Helping Businesses And Individuals Realize A Return On<br>Investment By Implementing Today's Advanced Technologies.</div>

<h2 class="section-title welcome-title abs">WELCOME TO <span class="brand"><span class="brand-mark"></span>VELMARKETA</span></h2>
<h3 class="welcome-sub abs">BOTTOM LINE BENEFITS FROM <span>OUTSOURCING TECHNOLOGY</span></h3>
<div class="welcome-copy abs">
  <p class="lead">In today's world, companies are expected to use technology to function and stay competitive. However, this aspect of business provides many challenges that most companies cannot solve on their own. Outsourcing technology provides solutions to almost every aspect of your business and can increase your profits.</p>
  <p>Outsourcing can save your business time, effort and can reduce the need for infrastructure and manpower. Outsourcing removes the burden of an ever-changing infrastructure, which is dictated by the constantly changing world of technological advances. It can also lessen the need for hiring more employees, which in turn will save on all related training costs for your firm. These savings will help bring about an increase in your revenue. Another aspect companies must deal with is growth. This sometimes leads to a shift in focus and priorities. However, the main focus of any size firm should be providing service and core functions to its clients</p>
</div>
<div class="btn-outline abs">Read More <svg width="10" height="12" viewBox="0 0 10 12"><path d="M0 0l10 6-10 6z" fill="#333"/></svg></div>
<div class="divider abs" style="top:1135px"></div>

<h2 class="section-title services-title abs">OUR SERVICES</h2>
<p class="services-intro abs">Lorem ipsum dolor sit amet consetug e sed diay nibh euismodl tincidunt ut laoreet dolore magam er vol wisi enim ad minim veniam quis nostrud exerci tationorem ipsum dolor sit ametee sed diammmy nibh euismd tincidunt ut laoreet dolore magna aliqur.</p>

<div class="service abs" style="top:1318px;left:440px;width:320px;text-align:center">
  <h3>IT Consulting</h3>Lorem ipsum dolor sit amet consetug e sed ut laoreet dolore magam er vol wisi enim.
</div>
<div class="service support abs" style="top:1544px;left:100px;width:260px;text-align:center">
  <h3>Support</h3>Lorem ipsum dolor sit amet sed ut laoreet dolore magam er vol wisi enim.
</div>
<div class="service abs" style="top:1544px;left:852px;width:260px">
  <h3>Management</h3>Lorem ipsum dolor sit amet sed ut laoreet dolore magam er vol wisi enim.
</div>

<svg class="abs" style="top:1400px;left:380px" width="440" height="278" viewBox="0 0 440 278">
  <path d="M40 278 A180 170 0 0 1 400 278" fill="none" stroke="#9a9a9a" stroke-width="1.5"/>
  <line x1="220" y1="76" x2="220" y2="108" stroke="#9a9a9a" stroke-width="1.5"/>
  <circle cx="220" cy="40" r="34" fill="#fff" stroke="#555" stroke-width="2"/>
  <circle cx="220" cy="30" r="5" fill="#222"/><circle cx="205" cy="44" r="5" fill="#222"/><circle cx="235" cy="44" r="5" fill="#222"/>
  <rect x="202" y="52" width="36" height="4" fill="#222"/>
  <circle cx="220" cy="108" r="5" fill="#fff" stroke="#f07f1e" stroke-width="2"/>
  <circle cx="92" cy="160" r="5" fill="#fff" stroke="#f07f1e" stroke-width="2"/>
  <circle cx="348" cy="160" r="5" fill="#fff" stroke="#f07f1e" stroke-width="2"/>
  <rect x="194" y="162" width="52" height="52" fill="#f07f1e"/>
  <circle cx="35" cy="190" r="34" fill="#fff" stroke="#f07f1e" stroke-width="2"/>
  <rect x="20" y="178" width="26" height="18" fill="none" stroke="#777" stroke-width="2"/>
  <path d="M30 200h6M42 190l12 12" stroke="#777" stroke-width="2"/>
  <circle cx="405" cy="190" r="34" fill="#fff" stroke="#555" stroke-width="2"/>
  <circle cx="405" cy="190" r="6" fill="#222"/>
  <circle cx="405" cy="172" r="4" fill="#222"/><circle cx="405" cy="208" r="4" fill="#222"/><circle cx="387" cy="190" r="4" fill="#222"/><circle cx="423" cy="190" r="4" fill="#222"/>
  <path d="M405 176v8M405 196v8M391 190h8M411 190h8" stroke="#222" stroke-width="2"/>
  <path d="M40 278v-6M400 278v-6" stroke="#9a9a9a" stroke-width="3"/>
</svg>

<section class="gallery abs"></section>
<h2 class="section-title gallery-title abs">PROJECT GALLERY</h2>
<svg class="side-arrow abs" style="top:1850px;left:98px" viewBox="0 0 14 24"><path d="M11 2 3 12l8 10" stroke="#777" stroke-width="2" fill="none"/></svg>
<svg class="side-arrow abs" style="top:1850px;left:1088px" viewBox="0 0 14 24"><path d="M3 2l8 10-8 10" stroke="#222" stroke-width="2" fill="none"/></svg>
<div class="gallery-item abs" style="left:130px">
  <div class="gallery-photo" role="img" aria-label="Two engineers checking a server rack" style="background:linear-gradient(135deg,#9fb4c8,#3f5a78)"></div>
  <p>Lorem ipsum dolor sit amet con setug e sed diay nibh euism</p>
</div>
<div class="gallery-item active abs" style="left:368px">
  <div class="gallery-photo" role="img" aria-label="Project sketch on a desk, dimmed with a project name overlay" style="background:linear-gradient(135deg,#6a6a6a,#3a3a3a)"><span>Project Name</span></div>
  <p>Lorem ipsum dolor sit amet con setug e sed diay nibh euism</p>
</div>
<div class="gallery-item abs" style="left:616px">
  <div class="gallery-photo" role="img" aria-label="Glowing blue network grid" style="background:linear-gradient(135deg,#0a1a4a,#1f5fd6 55%,#08133a)"></div>
  <p>Lorem ipsum dolor sit amet con setug e sed diay nibh euism</p>
</div>
<div class="gallery-item abs" style="left:856px">
  <div class="gallery-photo" role="img" aria-label="Business team meeting around a laptop" style="background:linear-gradient(135deg,#d8d6d2,#6c6258)"></div>
  <p>Lorem ipsum dolor sit amet con setug e sed diay nibh euism</p>
</div>

<h2 class="section-title testi-title abs">CLIENT TESTIMONIALS</h2>
<svg class="side-arrow abs" style="top:2242px;left:78px" viewBox="0 0 14 24"><path d="M11 2 3 12l8 10" stroke="#ccc" stroke-width="2" fill="none"/></svg>
<svg class="side-arrow abs" style="top:2242px;left:1110px" viewBox="0 0 14 24"><path d="M3 2l8 10-8 10" stroke="#ccc" stroke-width="2" fill="none"/></svg>
<div class="testi-card abs" style="left:100px"><span class="q">“</span>Lorem ipsum dolor sit amet consetug e sed diay nibh euismodl tincidunt ut laoreet dolore magam er vol wisi enim ad minim veniam quis nostrud exerci tationorem ipsum dolor sit ametee sed diammmy nibh euismd tincidunt ut laoreet dolore magna aliqur volpat! tiidunt ut laoreet dolore magna aliqur volpat! Lorem ipsum dolor sit amet consetug e sed diay nibh euismodl tincidunt ut laoreet dolore magam er vol</div>
<div class="testi-card abs" style="left:622px"><span class="q">“</span>Lorem ipsum dolor sit amet consetug e sed diay nibh euismodl tincidunt ut laoreet dolore magam er vol wisi enim ad minim veniam quis nostrud exerci tationorem ipsum dolor sit ametee sed diammmy nibh euismd tincidunt ut laoreet dolore magna aliqur volpat! tiidunt ut laoreet dolore magna aliqur volpat! Lorem ipsum dolor sit amet consetug e sed diay nibh euismodl tincidunt ut laoreet dolore magam er vol</div>
<div class="avatar abs" style="left:128px;background:linear-gradient(160deg,#c9b8a6,#6b5a4c)" role="img" aria-label="Client portrait photo"></div>
<div class="avatar abs" style="left:652px;background:linear-gradient(160deg,#d4c2ae,#7a6654)" role="img" aria-label="Client portrait photo"></div>
<div class="testi-name abs" style="left:306px">Mr.Alden Marsh</div>
<div class="testi-name abs" style="left:828px">Mr.Alden Marsh</div>
<div class="divider abs" style="top:2487px"></div>

<h2 class="section-title news-title abs">LATESTS NEWS</h2>
<svg class="side-arrow abs" style="top:2670px;left:78px" viewBox="0 0 14 24"><path d="M11 2 3 12l8 10" stroke="#ccc" stroke-width="2" fill="none"/></svg>
<svg class="side-arrow abs" style="top:2670px;left:1110px" viewBox="0 0 14 24"><path d="M3 2l8 10-8 10" stroke="#ccc" stroke-width="2" fill="none"/></svg>
<article class="news-card abs" style="left:97px">
  <div class="news-photo" role="img" aria-label="Businessman touching a glowing network diagram" style="background:radial-gradient(circle at 50% 45%,#e0a067,#5a3a22 45%,#1a1410)"></div>
  <div class="news-body"><div class="news-date"><b>24</b><i>FEB</i></div><h4>Lorem ipsum dolor sit amet,</h4><div class="news-meta">by <span>admin</span> - in news, IT</div>Ut wisi enim ad minim veniam, quisvero exerci tation ullamcorper.</div>
</article>
<article class="news-card abs" style="left:441px">
  <div class="news-photo" role="img" aria-label="Close-up of a circuit board and microchip" style="background:radial-gradient(circle at 50% 50%,#4fc0e8,#0d4a6a 45%,#04141f)"></div>
  <div class="news-body"><div class="news-date"><b>24</b><i>FEB</i></div><h4>Lorem ipsum dolor sit amet,</h4><div class="news-meta">by <span>admin</span> - in news, IT</div>Ut wisi enim ad minim veniam, quisvero exerci tation ullamcorper.</div>
</article>
<article class="news-card abs" style="left:785px">
  <div class="news-photo" role="img" aria-label="Backlit blue keyboard keys" style="background:linear-gradient(160deg,#0a1a40,#2f6fd8 55%,#08102a)"></div>
  <div class="news-body"><div class="news-date"><b>24</b><i>FEB</i></div><h4>Lorem ipsum dolor sit amet,</h4><div class="news-meta">by <span>admin</span> - in news, IT</div>Ut wisi enim ad minim veniam, quisvero exerci tation ullamcorper.</div>
</article>

<section class="callback abs"></section>
<h2 class="abs" style="top:3026px;left:100px;font-family:'Russo One',sans-serif;font-weight:400;font-size:36px;line-height:42px;color:var(--ink)">REQUEST<br>A CALL BACK.</h2>
<p class="callback-copy abs">Duis autem vel eum iriure dolormi opl inmokl hendi rerit in vulpu tateml velitm essemol mo molestiel conseqb uat, velmi illum dolor eokf no atn nulla more facilisis... [+]</p>
<div class="form-label abs">Please fill up bellow form</div>
<div class="field abs" style="top:3058px;left:458px">Name</div>
<div class="field abs" style="top:3058px;left:786px">Email</div>
<div class="field abs" style="top:3108px;left:458px">Phone</div>
<div class="field abs" style="top:3108px;left:786px">Message</div>
<div class="submit abs">Submit</div>

<footer class="site-footer abs" role="img" aria-label="Dark circuit board background"></footer>
<div class="footer-contact abs" style="left:150px">
  <svg width="18" height="24" viewBox="0 0 18 24"><path d="M9 23S2 13 2 8.5a7 7 0 0 1 14 0C16 13 9 23 9 23z" fill="none" stroke="#f07f1e" stroke-width="2"/><circle cx="9" cy="8.5" r="2.5" fill="#f07f1e"/></svg>
  12 Lorem ipsum dolor 456 Sed diam, nonummy
</div>
<div class="footer-contact abs" style="left:440px">
  <svg width="22" height="22" viewBox="0 0 24 24"><path d="M6 2l4 5-2 3c1.5 3 3 4.5 6 6l3-2 5 4-2 4C11 21 3 13 2 4z" fill="none" stroke="#f07f1e" stroke-width="2"/></svg>
  Phone: (00) 123-456-7890
</div>
<div class="footer-contact abs" style="left:730px">
  <svg width="24" height="22" viewBox="0 0 24 22"><path d="M2 11 22 2l-5 18-6-6zM11 14v6l3-3" fill="none" stroke="#f07f1e" stroke-width="2"/></svg>
  Email: info@velmarketa.com
</div>
<div class="footer-brand abs"><div class="brand"><span class="brand-mark" style="width:34px;height:34px"></span>VELMARKETA</div></div>
<div class="social abs"><span></span><span></span><span></span><span></span></div>
<div class="copyright abs">Copyright © 2017 velmarketa.com . All Right Reserved.</div>

</body>
</html>
```